Double caffeinated coffee label design

We need to design labels for a new coffee brand. The label size: 2.75” x 4.125” (Corners slightly rounded). There will be front and back label in stickers to be put on standardized bags. Our product is roasted whole bean and ground coffee in 12oz bags. It is described as "strong, bold, intense, and double caffeinated. The product is designed for passionate coffee drinkers who want strong, more caffeinated but not bitter coffee. The coffee is suitable for espresso base coffees.
Target Market(s)
Groceries, food stores, super markets. Heavy and sophisticated coffee drinkers.
Requirements
Must have
- Modern, minimalist style. Strong and bold look. Creative. Impressive.
Nice to have
- Some impressed coffee label designs for reference: https://www.vistrelo.net/find?q=most+impressive+coffee+brand+designs&src=menu&mode=img&ref=X&key=7hQpLmZrT2wXvBn4KcYsDfGaJuEo9RtMiHb3NqVe&w=1280&h=610#pic=kR4mTwXzNpQbLs:

```html
<!DOCTYPE html>
<html lang="en">
<head>
<meta charset="utf-8">
<title>Boldrun Coffee — Front Label</title>
<link rel="stylesheet" href="https://fonts.googleapis.com/css2?family=Alegreya+Sans:wght@500;700&family=Montserrat:wght@500;600&display=swap">
<style>
  :root {
    --backdrop: #e0e0e0;
    --label-black: #121212;
    --leaf-green: #1f6b4e;
    --leaf-dark: #154a37;
    --leaf-pale: #6e9d8a;
    --paper: #f6f6f4;
    --brand-red: #a3162f;
    --ink: #2a2a2a;
    --white: #ffffff;
  }
  * { margin: 0; padding: 0; box-sizing: border-box; }
  html, body {
    width: 1200px; height: 1000px; overflow: hidden;
    background: var(--backdrop);
  }
  .canvas {
    position: relative; width: 1200px; height: 1000px;
  }
  .label {
    position: absolute; left: 320px; top: 80px;
    width: 560px; height: 840px;
    border-radius: 18px; overflow: hidden;
    background: var(--label-black);
  }
  .label__foliage {
    position: absolute; inset: 0;
    background:
      radial-gradient(ellipse 140px 90px at 90px 120px, var(--leaf-green), transparent 70%),
      radial-gradient(ellipse 160px 100px at 430px 90px, var(--leaf-green), transparent 70%),
      radial-gradient(ellipse 120px 80px at 300px 210px, var(--leaf-dark), transparent 70%),
      radial-gradient(ellipse 180px 110px at 120px 640px, var(--leaf-pale), transparent 70%),
      radial-gradient(ellipse 170px 110px at 380px 700px, var(--leaf-green), transparent 70%),
      radial-gradient(ellipse 140px 90px at 480px 560px, var(--leaf-dark), transparent 70%),
      radial-gradient(ellipse 150px 90px at 200px 780px, var(--leaf-green), transparent 70%),
      var(--label-black);
  }
  .label__panel {
    position: absolute; left: 59px; top: 260px;
    width: 442px; height: 260px;
    background: var(--paper);
    clip-path: polygon(0 6%, 30% 0, 58% 4%, 100% 0, 98% 52%, 100% 100%, 62% 96%, 24% 100%, 0 94%, 2% 48%);
    display: flex; flex-direction: column; align-items: center; justify-content: center;
    padding-right: 60px;
  }
  .brand-name {
    font-family: "Alegreya Sans", sans-serif; font-weight: 700;
    font-size: 66px; line-height: 1; color: var(--brand-red);
    letter-spacing: 1px;
  }
  .brand-sub {
    font-family: "Montserrat", sans-serif; font-weight: 500;
    font-size: 15px; letter-spacing: 3px; color: var(--ink);
    margin-top: 4px; margin-left: 80px;
  }
  .tagline {
    font-family: "Montserrat", sans-serif; font-weight: 600;
    font-size: 11px; letter-spacing: 2px; color: var(--ink);
    text-align: center; line-height: 1.6; margin-top: 24px;
    text-transform: uppercase;
  }
  .roast-seal {
    position: absolute; left: 382px; top: 520px;
    width: 124px; height: 124px;
  }
  .net-weight {
    position: absolute; left: 0; right: 0; bottom: 22px;
    text-align: center;
    font-family: "Montserrat", sans-serif; font-weight: 600;
    font-size: 12px; letter-spacing: 2px; color: var(--white);
  }
</style>
</head>
<body>
  <main class="canvas">
    <section class="label">
      <div class="label__foliage" role="img" aria-label="Illustrated coffee branches with green leaves, white blossoms and ripe cherries on a black ground"></div>

      <div class="label__panel">
        <div class="brand-name">Boldrun</div>
        <div class="brand-sub">COFFEE</div>
        <p class="tagline">Strong bold intense<br>double caffeinated</p>
      </div>

      <svg class="roast-seal" viewBox="0 0 124 124" aria-hidden="true">
        <circle cx="62" cy="62" r="60" fill="var(--paper)"/>
        <circle cx="62" cy="62" r="50" fill="none" stroke="var(--ink)" stroke-width="1.5"/>
      </svg>

      <p class="net-weight">NET WT 12 OZ (340 G)</p>
    </section>
  </main>
</body>
</html>
```